Business Card Design

I need Business card designs with following on cards:

Dorian Felsk
Director

M: +61 491 208 356
D: +61 7 5580 1926
F: +61 7 5580 6471
E: dorian@mevrostrand.example.au

Mevro Group
Suite 4/61 North Calloway Road
Tindall Point QLD 4299

Ross Halvorn
Director

M: +61 438 902 615
D: +61 7 5580 1926
F: +61 7 5580 6471
E: ross@mevrostrand.example.au

Mevro Group
Tindall Point QLD 4299

Mevro Group Logo has been attached to brief.

Industry/Entity Type

Business

```html
<!DOCTYPE html>
<html lang="en">
<head>
<meta charset="utf-8">
<title>Mevro Group – Business Card</title>
<link href="https://fonts.googleapis.com/css2?family=Open+Sans:wght@400&family=Arimo:wght@400&display=swap" rel="stylesheet">
<style>
  :root {
    --white: #ffffff;
    --ink: #111111;
    --muted: #555a60;
    --name-red: #e8120c;
    --card-red: #dd1500;
    --orange: #e54800;
    --amber: #ef8c00;
    --gold: #f3ad14;
  }
  * { margin: 0; padding: 0; box-sizing: border-box; }
  html, body { width: 1050px; height: 1200px; overflow: hidden; background: var(--white); }
  .sheet { position: relative; width: 1050px; height: 1200px; }

  .card-front { position: absolute; left: 0; top: 0; width: 1050px; height: 600px; background: var(--white); overflow: hidden; }
  .front-accent {
    position: absolute; left: 600px; top: 0; width: 450px; height: 600px;
    background: linear-gradient(180deg, var(--gold) 0%, var(--amber) 35%, var(--orange) 55%, var(--card-red) 80%);
  }

  .brand { position: absolute; display: flex; align-items: center; font-family: "Open Sans", sans-serif; font-size: 66px; font-weight: 400; line-height: 1; white-space: nowrap; }
  .brand-dot { width: 104px; height: 104px; border-radius: 50%; flex: none; }
  .brand-text { position: relative; top: -20px; }
  .brand-front { left: 51px; top: 46px; color: var(--ink); }
  .brand-front .brand-dot { background: var(--amber); margin-right: 23px; }

  .holder-name { position: absolute; left: 54px; top: 166px; font-family: "Open Sans", sans-serif; font-size: 52px; font-weight: 400; line-height: 1; color: var(--name-red); }
  .holder-role { position: absolute; left: 55px; top: 225px; font-family: "Arimo", sans-serif; font-size: 22px; line-height: 1; color: var(--muted); }

  .contact-list, .address { position: absolute; font-family: "Arimo", sans-serif; font-size: 23px; line-height: 34px; color: var(--ink); list-style: none; }
  .contact-list { left: 53px; top: 308px; }
  .address { left: 46px; top: 492px; font-style: normal; }

  .card-back { position: absolute; left: 0; top: 622px; width: 1050px; height: 578px; background: var(--card-red); }
  .brand-back { left: 320px; top: 238px; color: var(--white); }
  .brand-back .brand-dot { background: var(--white); margin-right: 24px; }
</style>
</head>
<body>
<main class="sheet">
  <section class="card-front">
    <div class="front-accent" role="img" aria-label="Decorative warm colour area in gold, orange and red"></div>

    <div class="brand brand-front"><span class="brand-dot"></span><span class="brand-text">Mevro Group</span></div>

    <h1 class="holder-name">Ross Halvorn</h1>
    <p class="holder-role">Director</p>

    <ul class="contact-list">
      <li>M - +61 438 902 615</li>
      <li>D - +61 7 5580 1926</li>
      <li>F - +61 7 5580 6471</li>
      <li>E - ross@mevrostrand.example.au</li>
    </ul>

    <address class="address">
      Mevro Group<br>
      Suite 4/61 North Calloway Road<br>
      Tindall Point QLD 4299
    </address>
  </section>

  <section class="card-back">
    <div class="brand brand-back"><span class="brand-dot"></span><span class="brand-text">Mevro Group</span></div>
  </section>
</main>
</body>
</html>
```